Website to promote New Zealand as a destination by BKR

We are a company that promotes New Zealand education, migration, business and travel opportunities. We want a website to reflect all these activities. We have an existing website that should be used as a base template and add the other required pages to it. The current website is what we want to expand upon. Access to the files of the current website may not be possible since the previous designer cannot be contacted. So the new designer has to use the existing template and build the whole thing from there. It should be an easy job since there is already a clear sample of what we want. I would like the same flow to continue where the impact is very high visually and very little text content. I expect most clients to use a mobile device to access the site. so it has to be extremely mobile friendly.
Updates

Target Market(s)

Anybody between ages of 16-60 who would like to study, settle, work, travel or invest in New Zealand.

Industry/Entity Type

Education

Contact Information for Business Card

Devan Mirza
Licensed Immigration Adviser
License No 308741925

Mob: +64 219837462
Email: devan.mirza@bkrgroup.example
BKR Services Limited
417 Tanner Lane
Ashbury
Hamilton
New Zealand - 3210

www.bkrgroup.example

Coding

Coded - Design and coding required

Number of Pages Required

5+ page

Font styles to use
Sans Serif

Requirements
Must have
• MUST use the existing design of our website and build other pages from it.
Should not have
• Nil

```html
<!DOCTYPE html>
<html lang="en">
<head>
<meta charset="utf-8">
<title>BKR Group – Our Services</title>
<link href="https://fonts.googleapis.com/css2?family=Open+Sans:wght@400;600;700&family=Lato:wght@300;400;700&display=swap" rel="stylesheet">
<style>
:root{
  --bar:#2a2a2a;
  --ink:#3a2350;
  --tab-active:#3b2150;
  --pink:#e98bb0;
  --btn-top:#f6b3cb;
  --btn-bottom:#e97fa5;
  --text:#5f5f5f;
  --white:#ffffff;
  --cta:#f0185f;
  --foot:#141214;
}
*{box-sizing:border-box;margin:0;padding:0}
html,body{width:1200px;height:3109px;overflow:hidden}
body{position:relative;font-family:"Open Sans",Arial,sans-serif;background:var(--white);color:var(--text)}
.abs{position:absolute}

/* header */
.site-header{left:0;top:0;width:1200px;height:70px;background:var(--bar)}
.brand{left:77px;top:18px;display:flex;align-items:center;gap:10px;color:var(--white);font-weight:700;font-size:22px;letter-spacing:1px}
.brand-dot{width:30px;height:30px;border-radius:50%;background:var(--white)}
.main-nav{top:27px;left:0;width:1200px;height:20px}
.main-nav span{position:absolute;color:#e8e8e8;font-size:13px;letter-spacing:.3px;white-space:nowrap}
.main-nav small{font-size:8px;color:#aaa;margin-left:4px;vertical-align:2px}

/* hero */
.hero{left:0;top:70px;width:1200px;height:353px;background:linear-gradient(180deg,#54409a 0%,#4a3890 45%,#3a2f7a 75%,#2a2560 100%)}
.hero-title{left:0;top:212px;width:1200px;text-align:center;color:var(--white);font-size:52px;font-weight:400;letter-spacing:2px}

/* tabs */
.service-tabs{left:75px;top:444px;width:1050px;height:107px;display:flex;gap:4px}
.tab{flex:1;border:2px solid var(--pink);background:var(--white);display:flex;flex-direction:column;align-items:center;justify-content:flex-end;padding-bottom:18px;gap:12px;color:var(--ink);font-size:13px;font-weight:700;letter-spacing:.5px}
.tab svg{width:44px;height:40px;fill:#7a7a7a}
.tab.is-active{background:var(--tab-active);border-color:var(--tab-active);color:var(--white)}
.tab.is-active svg{fill:var(--white)}

/* service rows */
.band{left:0;width:1200px}
.band.grey{background:linear-gradient(180deg,#e8e8e8 0%,#f6f6f6 100%)}
.photo{width:512px;height:304px;border:2px solid var(--pink)}
.service-title{color:var(--ink);font-size:23px;font-weight:700;letter-spacing:1px}
.service-text{width:512px;font-size:15.2px;line-height:28px;color:var(--text)}
.read-more{width:152px;height:44px;background:linear-gradient(180deg,var(--btn-top),var(--btn-bottom));color:var(--ink);font-size:13px;font-weight:700;letter-spacing:.5px;display:flex;align-items:center;justify-content:center;border-radius:2px}

/* contact */
.contact{left:0;top:2555px;width:1200px;height:502px;background:radial-gradient(ellipse at 60% 35%,#6a2a7a 0%,#3b1848 45%,#1e0c26 100%)}
.contact-title{left:0;top:2617px;width:1200px;text-align:center;font-family:"Lato",Arial,sans-serif;font-weight:400;font-size:54px;color:var(--white)}
.field{background:rgba(70,40,110,.75);color:#a79ab6;font-size:14px;padding:10px 14px;font-family:Arial,sans-serif}
.enquire{left:385px;top:2935px;width:150px;height:39px;background:var(--cta);color:var(--white);font-size:16px;display:flex;align-items:center;justify-content:center;border-radius:3px;font-family:Arial,sans-serif}
.office{left:891px;top:2730px;color:var(--white);font-size:13px;line-height:25px;font-style:normal}
.office h3{font-size:20px;font-weight:700;margin-bottom:10px}
.social{left:891px;top:2898px;display:flex;gap:10px}
.social span{width:37px;height:37px;border-radius:50%;background:var(--white)}

.site-footer{left:0;top:3057px;width:1200px;height:52px;background:var(--foot);color:#6a6a6a;font-size:11px;text-align:center;line-height:52px}
.site-footer b{color:#9a9a9a;font-weight:600}
</style>
</head>
<body>

<header class="abs site-header">
  <div class="abs brand"><span class="brand-dot"></span>BKR Group</div>
  <nav class="abs main-nav">
    <span style="left:613px">HOME<small>▾</small></span>
    <span style="left:694px">MIGRATION SERVICES<small>▾</small></span>
    <span style="left:881px">INFOTECH SERVICES<small>▾</small></span>
    <span style="left:1057px">CONTACT</span>
  </nav>
</header>

<section class="abs hero" role="img" aria-label="City skyline with harbour tower under a purple tint"></section>
<h1 class="abs hero-title">OUR SERVICES</h1>

<div class="abs service-tabs">
  <div class="tab is-active">
    <svg viewBox="0 0 44 40"><path d="M22 6 2 15l20 9 16-7.2V28h3V15z"/><path d="M10 21v8c0 3 5.5 6 12 6s12-3 12-6v-8l-12 5.4z"/></svg>EDUCATION</div>
  <div class="tab">
    <svg viewBox="0 0 44 40"><path d="M22 6a14 14 0 0 1 12.5 7.7L38 10v11H27l4.6-4.6A10 10 0 0 0 12.3 17H8.2A14 14 0 0 1 22 6zM22 34a14 14 0 0 1-12.5-7.7L6 30V19h11l-4.6 4.6A10 10 0 0 0 31.7 23h4.1A14 14 0 0 1 22 34z"/></svg>MIGRATION</div>
  <div class="tab">
    <svg viewBox="0 0 44 40"><path d="M8 8h28v20H8zm3 3v14h22V11z"/><path d="M2 30h40v2a2 2 0 0 1-2 2H4a2 2 0 0 1-2-2z"/></svg>WORK</div>
  <div class="tab">
    <svg viewBox="0 0 44 40"><path d="M16 6h12a2 2 0 0 1 2 2v4h-3V9H17v3h-3V8a2 2 0 0 1 2-2z"/><rect x="4" y="13" width="36" height="22" rx="3"/></svg>BUSINESS</div>
  <div class="tab">
    <svg viewBox="0 0 44 40"><path d="M38 4c2 2-1 6-4 9l-5 5 4 16-3 3-7-12-6 6 1 6-2 2-3-6-6-3 2-2 6 1 6-6-12-7 3-3 16 4 5-5c3-3 7-6 9-4z"/></svg>TRAVEL</div>
</div>

<div class="abs photo" style="left:75px;top:587px;background:linear-gradient(135deg,#c9b8a8,#8a7a6e 55%,#4a4642)" role="img" aria-label="Students writing at desks in a classroom"></div>
<h2 class="abs service-title" style="left:613px;top:620px">EDUCATION</h2>
<p class="abs service-text" style="left:613px;top:662px">New Zealand provides quality education that matches international standards. Education opportunities in New Zealand start from primary school all the way up to a PhD. One unique feature of the New Zealand education system at the tertiary level is the opportunity...</p>
<div class="abs read-more" style="left:613px;top:808px">READ MORE</div>

<section class="abs band grey" style="top:935px;height:383px"></section>
<h2 class="abs service-title" style="left:75px;top:1016px">MIGRATION</h2>
<p class="abs service-text" style="left:75px;top:1058px">New Zealand provides an amazing opportunity to make this beautiful country your home as a long term migrant. Migration opportunities in New Zealand are many starting with Skilled Migrant Category, Business Category and Family Categories....</p>
<div class="abs read-more" style="left:75px;top:1206px">READ MORE</div>
<div class="abs photo" style="left:613px;top:984px;background:linear-gradient(180deg,#9fb4d4 0%,#6d7f8e 45%,#6e8a3e 100%)" role="img" aria-label="Backpackers walking across a grassy field"></div>

<div class="abs photo" style="left:75px;top:1384px;background:linear-gradient(135deg,#e8e2d4,#b8a488 50%,#5a4a40)" role="img" aria-label="Young professional working on a laptop"></div>
<h2 class="abs service-title" style="left:613px;top:1416px">WORK</h2>
<p class="abs service-text" style="left:613px;top:1458px">New Zealand seeks to attract high quality professionals to address our skill shortage areas. Currently we have Long Term Skill Shortages in areas like Agriculture and Forestry, Construction, Engineering, Finance/Business, Health and Social Services..</p>
<div class="abs read-more" style="left:613px;top:1604px">READ MORE</div>

<section class="abs band grey" style="top:1733px;height:402px"></section>
<h2 class="abs service-title" style="left:75px;top:1814px">BUSINESS</h2>
<p class="abs service-text" style="left:75px;top:1856px">New Zealand is rated 2nd by the Global Trade Index out of 189 economies in their Ease of Doing Business survey. We offer a stable and dynamic environment for entrepreneurs to come to our country and set up your business.</p>
<div class="abs read-more" style="left:75px;top:2002px">READ MORE</div>
<div class="abs photo" style="left:613px;top:1782px;background:linear-gradient(135deg,#cfd8e0,#6c7888 50%,#23262e)" role="img" aria-label="Business people shaking hands at a meeting"></div>

<div class="abs photo" style="left:75px;top:2182px;background:linear-gradient(180deg,#5aa6e6 0%,#a8d4f2 45%,#d8e06a 70%,#4a8a3a 100%)" role="img" aria-label="World landmarks gathered on a globe under a blue sky"></div>
<h2 class="abs service-title" style="left:613px;top:2214px">TRAVEL</h2>
<p class="abs service-text" style="left:613px;top:2256px">New Zealand is also known as Godzone and the spectacular images from movies like Realm of Kings have already captivated audiences globally. We are also the adventure specialists of the world and continue to attract travellers...</p>
<div class="abs read-more" style="left:613px;top:2404px">READ MORE</div>

<section class="abs contact" role="img" aria-label="Dark purple and magenta background"></section>
<h2 class="abs contact-title">CONTACT US</h2>
<div class="abs field" style="left:104px;top:2736px;width:342px;height:41px">Name</div>
<div class="abs field" style="left:104px;top:2800px;width:342px;height:41px">Email</div>
<div class="abs field" style="left:104px;top:2864px;width:342px;height:42px">Phone</div>
<div class="abs field" style="left:473px;top:2736px;width:342px;height:172px">Text</div>
<div class="abs enquire">ENQUIRE</div>
<address class="abs office">
  <h3>BKR Group</h3>
  PO Box 40571,<br>Ashbury Post Shop,<br>Hamilton, Waikato,<br>New Zealand<br>Email: info@bkrgroup.example
</address>
<div class="abs social"><span></span><span></span><span></span><span></span></div>

<footer class="abs site-footer">© 2015 BKR Group | <b>Privacy Policy</b> | All rights reserved</footer>

</body>
</html>
```